Offshore Energy Projects Management Consultancy needs a business card design

Logo available. We provide teams to deliver engineering consultancy, project management and delivery teams mainly in the offshore renewables sector. The company is all about bringing the right people to a project to deliver the scope.

The business card will be used for all staff.

The business card should be quite simple, vibrant and uncluttered but convey experience, enthusiasm and integration.

Target Market(s)

Energy Project Developers and Tier 1 construction companies

Contact Information for Business Card

Logo should be on the back of the card. I'm happy for the designer to play with the colour of the logo and background colour.

Front of the card should convey all the must have information in a clear and professional manner but without being overly traditional.

Colors

Designer to choose colors to be used in the design.

Requirements
Must have
• Land Line Tel Number, Mobile Tel Number, Email, business address, web address.

```html
<!DOCTYPE html>
<html lang="en">
<head>
<meta charset="utf-8">
<title>Seaward Delivery Group – Business Card</title>
<link rel="stylesheet" href="https://fonts.googleapis.com/css2?family=Arimo:wght@400;700&display=swap">
<style>
  :root {
    --backdrop: #eeeeee;
    --card-white: #ffffff;
    --brand-blue: #1c78c4;
    --brand-sky: #23a3dc;
    --text-grey: #7a7a7a;
    --photo-light: #b9b9b9;
    --photo-mid: #8a8a8a;
    --photo-dark: #2c2c2c;
    --on-photo: #ffffff;
  }
  * { box-sizing: border-box; margin: 0; padding: 0; }
  html, body {
    width: 1200px; height: 686px; overflow: hidden;
    background: var(--backdrop);
    font-family: "Arimo", Arial, sans-serif;
  }
  .canvas {
    position: relative; width: 1200px; height: 686px;
    display: flex; justify-content: center; align-items: center; gap: 40px;
  }
  .card {
    position: relative; width: 540px; height: 309px; overflow: hidden;
    box-shadow: 0 2px 8px rgba(0,0,0,0.12);
  }

  /* Back of card */
  .card-back { background: var(--photo-dark); }
  .card-back__photo {
    position: absolute; inset: 0;
    background: linear-gradient(180deg, var(--photo-mid) 0%, var(--photo-light) 30%, #9d9d9d 50%, #5a5a5a 62%, var(--photo-dark) 100%);
  }
  .card-back__brand {
    position: absolute; left: 0; right: 0; top: 104px;
    display: flex; justify-content: center; align-items: center; gap: 14px;
  }
  .brand-dot {
    width: 38px; height: 38px; border-radius: 50%;
    background: var(--brand-sky);
  }
  .card-back__name {
    color: var(--on-photo); font-weight: 700; font-size: 30px;
    letter-spacing: 1px; text-transform: uppercase; line-height: 1.05;
  }
  .social-list {
    position: absolute; left: 0; right: 0; bottom: 26px;
    display: flex; justify-content: center; gap: 22px; list-style: none;
  }
  .social-list__item {
    display: flex; align-items: center; gap: 6px;
    color: var(--on-photo); font-size: 14px;
  }
  .social-list__dot {
    width: 14px; height: 14px; border-radius: 50%; background: var(--on-photo);
  }

  /* Front of card */
  .card-front { background: var(--card-white); }
  .card-front__web {
    position: absolute; left: 26px; top: 40px;
    color: var(--brand-sky); font-weight: 700; font-size: 15px;
  }
  .card-front__brand {
    position: absolute; right: 28px; top: 30px; text-align: right;
    color: var(--brand-blue); font-weight: 700; font-size: 17px;
    text-transform: uppercase; letter-spacing: 0.5px; line-height: 1.15;
  }
  .person {
    position: absolute; left: 26px; top: 168px;
  }
  .person__name { color: var(--text-grey); font-size: 20px; }
  .person__role { color: var(--brand-blue); font-weight: 700; font-size: 16px; margin-top: 3px; }
  .address {
    position: absolute; left: 26px; top: 232px;
    color: var(--text-grey); font-size: 14px; line-height: 1.3; font-style: normal;
  }
  .contact {
    position: absolute; left: 288px; top: 208px;
    color: var(--text-grey); font-size: 14px; line-height: 1.45; list-style: none;
  }
  .contact__label {
    display: inline-block; width: 22px;
    color: var(--brand-blue); font-weight: 700;
  }
</style>
</head>
<body>
<main class="canvas">
  <section class="card card-back" aria-label="Card back">
    <div class="card-back__photo" role="img" aria-label="Black and white photograph of an offshore wind farm at sea under a cloudy sky"></div>
    <div class="card-back__brand">
      <span class="brand-dot"></span>
      <span class="card-back__name">Seaward<br>Delivery Group</span>
    </div>
    <ul class="social-list">
      <li class="social-list__item"><span class="social-list__dot"></span>@SDGlimited</li>
      <li class="social-list__item"><span class="social-list__dot"></span>/SDG.ltd</li>
      <li class="social-list__item"><span class="social-list__dot"></span>company/sdgroup</li>
    </ul>
  </section>

  <section class="card card-front" aria-label="Card front">
    <p class="card-front__web">sdgroup.ltd</p>
    <p class="card-front__brand">Seaward<br>Delivery Group</p>
    <div class="person">
      <p class="person__name">Name Surname</p>
      <p class="person__role">Job Title</p>
    </div>
    <address class="address">
      The Harbourline Building,<br>
      72 Quay Street,<br>
      Aberdeen, AB10 1XY
    </address>
    <ul class="contact">
      <li><span class="contact__label">T:</span>+44(0) 1224 000 111</li>
      <li><span class="contact__label">M:</span>+44(0) 7700 900 123</li>
      <li><span class="contact__label">E:</span>name.surname@sdgroup.ltd</li>
    </ul>
  </section>
</main>
</body>
</html>
```